Corportate Power Point Template

We need a corporate PPT Design for our startup Big Data company.

Basically, our company will ingest, analyze and generate dynamic Dashboards with data consumed from different sources like Social Networks, Enterprise Legacy Systems such as e-Commerce, ERP, CRM and others.

Company is headquartered in Brazil, but will have a global presence.

Industry/Entity Type

It Company

```html
<!DOCTYPE html>
<html lang="en">
<head>
<meta charset="utf-8">
<title>Project Title Here</title>
<link href="https://fonts.googleapis.com/css2?family=Saira+Semi+Condensed:wght@400;500;600&family=Open+Sans:wght@400;600;700&display=swap" rel="stylesheet">
<style>
  :root {
    --orange: #f47b3a;
    --orange-strong: #ff7f32;
    --coral: #f57f48;
    --salmon: #f6a57f;
    --red: #e8391c;
    --ink: #444444;
    --text: #595959;
    --gray-light: #c0c0c0;
    --gray-mid: #7b7b7b;
    --gray-dark: #565656;
    --rule: #e2dcd8;
    --paper: #ffffff;
  }
  * { margin: 0; padding: 0; box-sizing: border-box; }
  html, body { width: 1200px; height: 900px; overflow: hidden; }
  body {
    position: relative;
    background:
      radial-gradient(ellipse 700px 420px at 380px 60px, rgba(255,190,150,0.28), rgba(255,255,255,0) 70%),
      linear-gradient(90deg, var(--paper) 0%, #fdfaf7 60%, #f7f5f4 100%);
    font-family: "Saira Semi Condensed", sans-serif;
    color: var(--text);
  }
  .title-accent {
    position: absolute; left: 0; top: 33px; width: 12px; height: 72px;
    background: var(--orange);
  }
  .slide-title {
    position: absolute; left: 36px; top: 24px;
    font-size: 56px; font-weight: 600; letter-spacing: 0.5px;
    color: var(--ink); line-height: 1.2;
  }
  .slide-title .highlight { color: var(--orange); }
  .content {
    position: absolute; left: 50px; top: 206px; width: 520px;
  }
  .content-heading {
    font-family: "Open Sans", sans-serif;
    font-size: 30px; font-weight: 400; color: var(--red);
    margin-bottom: 16px; letter-spacing: -0.3px;
  }
  .content p {
    font-size: 25px; line-height: 36px; text-align: justify;
    color: var(--text); margin-bottom: 36px; padding-left: 2px;
  }
  .pie { position: absolute; left: 0; top: 0; }
  .pie text {
    font-family: "Open Sans", sans-serif; font-weight: 700; font-size: 15px;
    text-anchor: middle;
  }
  .pie .on-dark { fill: #ffffff; }
  .pie .on-light { fill: #2f2f2f; }
  .footer-rule {
    position: absolute; left: 0; right: 0; top: 818px; height: 2px;
    background: var(--rule);
  }
  .presenter {
    position: absolute; left: 12px; top: 852px;
    font-size: 20px; color: #222;
  }
  .presenter .name { color: var(--orange); }
  .brand {
    position: absolute; right: 16px; top: 840px;
    display: flex; align-items: center; gap: 10px;
  }
  .brand-mark { width: 26px; height: 26px; background: var(--gray-dark); }
  .brand-name {
    font-size: 38px; font-weight: 500; color: var(--orange); line-height: 1;
  }
</style>
</head>
<body>
  <div class="title-accent"></div>
  <h1 class="slide-title"><span class="highlight">Project</span> Title Here</h1>

  <section class="content">
    <h2 class="content-heading">Lorem ipsum dolor sit ipsum</h2>
    <p>Lorem ipsum dolor sit ipsum Lorem ipsum dolor sit ipsum Lorem ipsum dolor sit ipsum Lorem ipsum dolor sit ipsum lorem ipsum dolor sit ipsum Lorem ipsum dolor sit ipsum Lorem ipsum dolor sit ipsum</p>
    <p>Lorem ipsum dolor sit ipsum Lorem ipsum dolor sit ipsum Lorem ipsum dolor sit ipsum Lorem ipsum dolor sit ipsum lorem ipsum dolor sit ipsum Lorem ipsum dolor sit ipsum Lorem ipsum dolor sit ipsum Lorem ipsum dolor sit ipsum</p>
  </section>

  <svg class="pie" width="1200" height="900" viewBox="0 0 1200 900" aria-label="Pie chart with six segments">
    <g stroke="#ffffff" stroke-width="2">
      <path d="M888 450 L888 220 A230 230 0 0 1 1023.2 263.9 Z" fill="var(--gray-light)"/>
      <path d="M888 450 L1023.2 263.9 A230 230 0 0 1 1105.8 523.7 Z" fill="var(--orange-strong)"/>
      <path d="M888 450 L1105.8 523.7 A230 230 0 0 1 970.4 664.7 Z" fill="var(--salmon)"/>
      <path d="M888 450 L970.4 664.7 A230 230 0 0 1 671.9 528.7 Z" fill="var(--coral)"/>
      <path d="M888 450 L671.9 528.7 A230 230 0 0 1 756.1 261.6 Z" fill="var(--gray-dark)"/>
      <path d="M888 450 L756.1 261.6 A230 230 0 0 1 888 220 Z" fill="var(--gray-mid)"/>
    </g>
    <circle cx="888" cy="452" r="35" fill="#ffffff" stroke="var(--red)" stroke-width="4.5"/>
    <text class="on-dark" x="845" y="286">Lorem<tspan x="845" dy="22">ipsum</tspan><tspan x="845" dy="22">dolor</tspan></text>
    <text class="on-light" x="934" y="286">Lorem<tspan x="934" dy="22">ipsum</tspan><tspan x="934" dy="22">dolor</tspan></text>
    <text class="on-light" x="1027" y="420">Lorem ipsum<tspan x="1027" dy="24">dolor</tspan></text>
    <text class="on-light" x="999" y="545">Lorem ipsum<tspan x="999" dy="24">dolor</tspan></text>
    <text class="on-light" x="825" y="560">Lorem ipsum dolor<tspan x="825" dy="24">Lorem ipsum dolor</tspan></text>
    <text class="on-dark" x="760" y="411">Lorem ipsum dolor<tspan x="760" dy="24">Lorem ipsum dolor</tspan></text>
  </svg>

  <div class="footer-rule"></div>
  <div class="presenter">Persentatator Name : <span class="name">Marcos Lindqvist</span></div>
  <div class="brand">
    <span class="brand-mark"></span>
    <span class="brand-name">Vertex Labs</span>
  </div>
</body>
</html>
```